Hybrid education and entertainment company needs help with creating dynamic school worksheets

I'm looking for a skilled individual to create a versatile Microsoft Word template for school worksheets for Lessonvibe. Your task will involve:
- Designing a user-friendly and visually appealing template that can be easily customized for various subjects and grade levels.
- Ensuring the template includes sections for titles, instructions, questions, and space for student responses.
- Incorporating consistent formatting and styles to maintain a professional look across all worksheets.
- Adding placeholders for images, graphics, or interactive elements to enhance engagement.
- Testing the template to ensure compatibility and ease of use for educators.
Your work will help streamline the worksheet creation process, making it easier for educators to develop effective and engaging learning materials.

```html
<!DOCTYPE html>
<html lang="en">
<head>
<meta charset="utf-8">
<title>Worksheet Template</title>
<link href="https://fonts.googleapis.com/css2?family=Poppins:wght@400;600;700;800&display=swap" rel="stylesheet">
<style>
  :root {
    --paper: #ffffff;
    --ink: #0a0c0b;
    --rule: #111111;
  }
  * { margin: 0; padding: 0; box-sizing: border-box; }
  html, body {
    width: 1000px;
    height: 1200px;
    overflow: hidden;
    background: var(--paper);
  }
  .worksheet {
    position: relative;
    width: 1000px;
    height: 1200px;
    background: var(--paper);
    color: var(--ink);
    font-family: "Poppins", sans-serif;
  }
  .worksheet > * { position: absolute; line-height: 1.2; white-space: nowrap; }

  .logo-slot {
    left: 140px; top: 112px;
    font-size: 36px; font-weight: 700; letter-spacing: -0.4px;
  }
  .meta {
    right: 126px; top: 159px;
    font-size: 23px; font-weight: 400;
    display: flex; flex-direction: column; gap: 7px;
  }
  .meta-field { display: flex; align-items: baseline; gap: 6px; }
  .meta-field .fill {
    display: inline-block;
    border-bottom: 2px dotted var(--ink);
    height: 1px;
  }
  .meta-field.date .fill { width: 139px; }
  .meta-field.grade .fill { width: 122px; }

  .title {
    left: 120px; top: 236px;
    font-size: 121px; font-weight: 800; letter-spacing: -1px;
  }

  .section-heading {
    left: 127px;
    font-weight: 700;
  }
  .instructions-heading { top: 392px; font-size: 37px; }
  .instructions-text {
    left: 126px; top: 448px;
    font-size: 27px; font-weight: 400;
  }
  .questions-heading { top: 511px; font-size: 40px; }

  .question-list {
    left: 128px; top: 579px;
    list-style: none;
    font-size: 18.5px; font-weight: 400;
  }
  .question-list li {
    display: flex; align-items: center; height: 54px;
  }
  .question-list .num { width: 30px; }

  .image-placeholder {
    left: 590px; top: 594px; width: 292px;
    text-align: center; font-weight: 700;
    font-size: 36px; line-height: 56px;
  }

  .long-answer-heading { top: 819px; font-size: 37px; }
  .answer-line {
    left: 127px; width: 757px; height: 2px;
    background: var(--rule);
  }
  .answer-line.l1 { top: 908px; }
  .answer-line.l2 { top: 955px; }
  .answer-line.l3 { top: 1001px; }

  .tagline {
    left: 0; width: 1004px; top: 1042px;
    text-align: center;
    font-size: 30px; font-weight: 400;
  }
  .page-number {
    right: 116px; top: 1100px;
    font-size: 24px; font-weight: 400;
  }
</style>
</head>
<body>
<main class="worksheet">
  <div class="logo-slot">LOGO PLACE</div>

  <div class="meta">
    <div class="meta-field date"><span>Date</span><span class="fill"></span></div>
    <div class="meta-field grade"><span>Grade</span><span class="fill"></span></div>
  </div>

  <h1 class="title">WORKSHEET</h1>

  <h2 class="section-heading instructions-heading">Instructions:</h2>
  <p class="instructions-text">Lorem ipsum dolor sit amet, consectetur adipiscing elit,</p>

  <h2 class="section-heading questions-heading">Questions:</h2>
  <ol class="question-list">
    <li><span class="num">1.</span><span>Lorem ipsum dolor sit amet, consectetur ?</span></li>
    <li><span class="num">2.</span><span>Lorem ipsum dolor sit amet, consectetur ?</span></li>
    <li><span class="num">3.</span><span>Lorem ipsum dolor sit amet, consectetur ?</span></li>
    <li><span class="num">4.</span><span>Lorem ipsum dolor sit amet, consectetur ?</span></li>
  </ol>

  <div class="image-placeholder">Insert<br>IMAGE HERE</div>

  <h2 class="section-heading long-answer-heading">Long Answer</h2>
  <div class="answer-line l1"></div>
  <div class="answer-line l2"></div>
  <div class="answer-line l3"></div>

  <p class="tagline">Engaging Learning Materials for All Grades</p>
  <p class="page-number">01</p>
</main>
</body>
</html>
```